Harwell Lawyers Banner

I would like to have a graphic design created for a company banner. The company is Harwell Lawyers and the website is https://harwelllawyers-example.com.au/ We would like a professional banner we are able to put up at events to advertise the company.
The banner size is 800mm wide by 2000mm high so please keep the design inside these constraints.

```html
<!DOCTYPE html>
<html lang="en">
<head>
<meta charset="utf-8">
<title>Harwell Lawyers – Event Banner</title>
<link rel="stylesheet" href="https://fonts.googleapis.com/css2?family=Anton&family=Montserrat:wght@500;600;700&display=swap">
<style>
  :root {
    --ink: #2b2e33;
    --blue: #07a6e3;
    --grey-text: #8a8a8a;
    --stripe: #e6e6e6;
    --white: #ffffff;
    --stage: #ededed;
  }
  * { margin: 0; padding: 0; box-sizing: border-box; }
  html, body { width: 1200px; height: 2414px; overflow: hidden; background: var(--stage); }
  body { position: relative; font-family: "Montserrat", sans-serif; }

  .banner {
    position: absolute; left: 169px; top: 139px;
    width: 922px; height: 2302px;
    transform: scale(0.9368); transform-origin: 0 0;
    background: var(--white); overflow: hidden;
  }
  .banner > * { position: absolute; }

  .header { left: 0; top: 0; width: 922px; height: 338px; background: var(--ink); }
  .brand { left: 0; top: 62px; width: 922px; text-align: center; color: var(--white); font-weight: 500; }
  .brand-name { display: block; font-size: 150px; line-height: 1; letter-spacing: 4px; white-space: nowrap; }
  .brand-sub { display: block; font-size: 50px; letter-spacing: 14px; margin-top: 18px; padding-left: 340px; }

  .accent-band { left: 0; top: 338px; width: 922px; height: 38px; background: var(--blue); }

  .quote-mark { top: 386px; font-family: "Anton", sans-serif; font-size: 70px; line-height: 1; color: #6b6e72; }
  .quote-open { left: 14px; }
  .quote-close { left: 868px; }
  .slogan { left: 0; top: 404px; width: 922px; text-align: center; font-family: "Anton", sans-serif; font-weight: 400; font-size: 138px; line-height: 1.1; color: var(--ink); white-space: nowrap; }
  .slogan em { font-style: normal; color: var(--blue); }
  .rule { top: 588px; height: 12px; border: 2px solid var(--blue); border-left: none; }
  .rule-left { left: 0; width: 72px; }
  .rule-right { left: 523px; width: 399px; border-left: 2px solid var(--blue); border-right: none; }

  .firm-band { left: 0; top: 610px; width: 922px; height: 121px; background: var(--ink); color: var(--white); font-weight: 700; font-size: 78px; line-height: 121px; text-align: center; letter-spacing: -1px; white-space: nowrap; }
  .tagline { left: 52px; top: 742px; font-weight: 700; font-size: 45px; color: var(--ink); letter-spacing: -0.5px; white-space: nowrap; }
  .spec-title { left: 53px; top: 830px; font-weight: 600; font-size: 31px; color: var(--grey-text); }

  .services { left: 0; top: 896px; width: 922px; list-style: none; }
  .services li { height: 38px; margin-bottom: 14px; display: flex; align-items: center; padding-left: 54px; font-weight: 500; font-size: 27px; color: var(--ink); white-space: nowrap; }
  .services li:nth-child(odd) { background: linear-gradient(90deg, var(--stripe), var(--stripe) 70%, rgba(230,230,230,0)); }
  .services svg { width: 22px; height: 22px; margin-right: 22px; flex: none; }

  .backdrop { left: 0; top: 1247px; width: 922px; height: 590px; background: linear-gradient(180deg, #ffffff 0%, #f1f2f3 45%, #dfe1e3 100%); }
  .portrait { left: 0; top: 1292px; width: 503px; height: 722px; background: linear-gradient(180deg, #c9b3a5 0%, #b89a88 40%, #2f3542 62%, #262b36 100%); }

  .name-plate { left: 472px; top: 1837px; width: 450px; height: 177px; }
  .name-box { left: 486px; top: 1874px; width: 420px; height: 52px; border: 2px solid var(--white); color: var(--white); font-weight: 700; font-size: 37px; line-height: 48px; text-align: right; padding-right: 18px; white-space: nowrap; }
  .role { left: 533px; top: 1934px; color: var(--white); font-weight: 600; font-size: 28px; line-height: 36px; letter-spacing: 1.5px; white-space: nowrap; }

  .contact { left: 0; top: 2014px; width: 922px; height: 208px; background: var(--ink); text-align: center; }
  .contact-call { display: block; margin-top: 22px; color: var(--blue); font-weight: 700; font-size: 46px; line-height: 56px; }
  .phone { display: flex; justify-content: center; align-items: center; gap: 18px; margin-top: 10px; color: var(--white); font-weight: 700; font-size: 104px; line-height: 110px; letter-spacing: -2px; white-space: nowrap; }
  .phone svg { width: 78px; height: 78px; }
  .website { left: 0; top: 2222px; width: 922px; height: 55px; line-height: 55px; text-align: center; font-weight: 600; font-size: 30px; letter-spacing: 5px; color: var(--ink); white-space: nowrap; }
  .footer-base { left: 0; top: 2277px; width: 922px; height: 25px; background: var(--ink); }
</style>
</head>
<body>
<main class="banner">
  <header class="header"></header>
  <div class="brand"><span class="brand-name">HARWELL</span><span class="brand-sub">LAWYERS</span></div>
  <div class="accent-band"></div>

  <span class="quote-mark quote-open">“</span>
  <span class="quote-mark quote-close">”</span>
  <h1 class="slogan">LET US <em>HELP YOU</em></h1>
  <div class="rule rule-left"></div>
  <div class="rule rule-right"></div>

  <h2 class="firm-band">HARWELL LAWYERS</h2>
  <p class="tagline">LEADING COMMERCIAL LAW FIRM</p>
  <p class="spec-title">Our Specialization</p>

  <ul class="services">
    <li><svg viewBox="0 0 22 22"><circle cx="10" cy="12" r="8" fill="none" stroke="#2b2e33" stroke-width="2"/><path d="M6 12l4 4 10-13" fill="none" stroke="#2b2e33" stroke-width="2.6"/></svg>Advising Family Businesses</li>
    <li><svg viewBox="0 0 22 22"><circle cx="10" cy="12" r="8" fill="none" stroke="#2b2e33" stroke-width="2"/><path d="M6 12l4 4 10-13" fill="none" stroke="#2b2e33" stroke-width="2.6"/></svg>Estate Planning, Administration &amp; Disputes</li>
    <li><svg viewBox="0 0 22 22"><circle cx="10" cy="12" r="8" fill="none" stroke="#2b2e33" stroke-width="2"/><path d="M6 12l4 4 10-13" fill="none" stroke="#2b2e33" stroke-width="2.6"/></svg>Tax and Structuring</li>
    <li><svg viewBox="0 0 22 22"><circle cx="10" cy="12" r="8" fill="none" stroke="#2b2e33" stroke-width="2"/><path d="M6 12l4 4 10-13" fill="none" stroke="#2b2e33" stroke-width="2.6"/></svg>Planning &amp; Environment</li>
    <li><svg viewBox="0 0 22 22"><circle cx="10" cy="12" r="8" fill="none" stroke="#2b2e33" stroke-width="2"/><path d="M6 12l4 4 10-13" fill="none" stroke="#2b2e33" stroke-width="2.6"/></svg>Not for Profit &amp; Social Enterprise</li>
    <li><svg viewBox="0 0 22 22"><circle cx="10" cy="12" r="8" fill="none" stroke="#2b2e33" stroke-width="2"/><path d="M6 12l4 4 10-13" fill="none" stroke="#2b2e33" stroke-width="2.6"/></svg>Management Rights, Property &amp; Developments</li>
    <li><svg viewBox="0 0 22 22"><circle cx="10" cy="12" r="8" fill="none" stroke="#2b2e33" stroke-width="2"/><path d="M6 12l4 4 10-13" fill="none" stroke="#2b2e33" stroke-width="2.6"/></svg>Litigation and Dispute Resolution</li>
  </ul>

  <div class="backdrop" role="img" aria-label="Faded city skyline with a large scales-of-justice silhouette"></div>
  <div class="portrait" role="img" aria-label="Portrait photo of the managing director in a dark suit and striped tie"></div>

  <svg class="name-plate" viewBox="0 0 450 177" aria-hidden="true"><polygon points="0,0 450,0 450,177 31,177" fill="#07a6e3"/></svg>
  <div class="name-box">DANIEL HARWELL</div>
  <p class="role">Managing Director &amp;<br>The Founder</p>

  <footer class="contact">
    <span class="contact-call">CONTACT US NOW!!</span>
    <div class="phone">
      <svg viewBox="0 0 78 78"><path d="M14 8c4-3 8-2 10 1l8 12c2 3 1 6-2 8l-5 3c3 8 10 16 19 20l3-5c2-3 5-4 8-2l12 8c3 2 4 6 1 10l-4 5c-4 4-10 5-16 2C28 62 15 48 8 30c-3-7-1-13 3-17z" fill="#fff"/><path d="M46 12a22 22 0 0 1 20 20M46 22a12 12 0 0 1 10 10" fill="none" stroke="#fff" stroke-width="5" stroke-linecap="round"/></svg>
      <span>07 3555 0142</span>
    </div>
  </footer>
  <p class="website">HARWELLLAWYERS-EXAMPLE.COM.AU</p>
  <div class="footer-base"></div>
</main>
</body>
</html>
```